"Willow Drift" Mattress Pad Packaging

We need packaging for a mattress pad. This will be sold through retailers across North America. We need something modern and clean, an update from what we currently have. This is targeted towards older women. I've attached what our current packaging looks like as well as other mattress pad packaging. This is a simple product so we're open to creativity and experimentation. This is our first time using this site so we're very open and hoping for something fun.

Font styles to use
Serif
Sans Serif

Colors

Designer to choose colors to be used in the design.

```html
<!DOCTYPE html>
<html lang="en">
<head>
<meta charset="utf-8">
<title>Willow Drift Mattress Pad Labels</title>
<link href="https://fonts.googleapis.com/css2?family=Cinzel:wght@400;700&family=Cormorant+Garamond:wght@400;600;700&display=swap" rel="stylesheet">
<style>
  :root {
    --gold-deep: #b8873d;
    --gold-light: #dcb877;
    --gold-text: #c49449;
    --silver-deep: #8f9093;
    --silver-light: #d8d9db;
    --silver-text: #a3a4a7;
    --paper: #fdfcf9;
    --satin-a: #f6f5f4;
    --satin-b: #dcdbdb;
    --satin-c: #ffffff;
    --canvas: #ffffff;
  }
  * { margin: 0; padding: 0; box-sizing: border-box; }
  html, body { width: 1075px; height: 1200px; overflow: hidden; background: var(--canvas); }
  .sheet { position: relative; width: 1075px; height: 1200px; }
  .proof-outline { position: absolute; left: 0; top: 0; width: 540px; height: 602px; border: 1px solid #222; }

  .label { position: absolute; width: 502px; height: 565px; border: 8px solid; }
  .label.gold { border-image: linear-gradient(90deg, var(--gold-light), var(--gold-deep), var(--gold-light), var(--gold-deep), var(--gold-light)) 1; --tone-a: var(--gold-deep); --tone-b: var(--gold-light); --solid: var(--gold-text); }
  .label.silver { border-image: linear-gradient(90deg, var(--silver-light), var(--silver-deep), var(--silver-light), var(--silver-deep), var(--silver-light)) 1; --tone-a: var(--silver-deep); --tone-b: var(--silver-light); --solid: var(--silver-text); }
  .pos-tl { left: 19px; top: 19px; }
  .pos-tr { left: 559px; top: 19px; }
  .pos-bl { left: 19px; top: 622px; }
  .pos-br { left: 559px; top: 622px; }

  .backdrop { position: absolute; inset: 0; }
  .backdrop.paper { background: var(--paper); }
  .backdrop.satin {
    background: linear-gradient(175deg, var(--satin-c) 0%, var(--satin-a) 18%, var(--satin-b) 30%, var(--satin-c) 42%, var(--satin-a) 60%, var(--satin-b) 72%, var(--satin-c) 82%, var(--satin-b) 92%, var(--satin-c) 100%);
  }

  .line { position: absolute; left: 0; right: 0; text-align: center; white-space: nowrap; }
  .metal {
    background: linear-gradient(90deg, var(--tone-a), var(--tone-b), var(--tone-a), var(--tone-b), var(--tone-a));
    -webkit-background-clip: text; background-clip: text; color: transparent;
  }
  .brand-mark { position: absolute; left: 50%; top: 43px; width: 60px; height: 60px; margin-left: -30px; border: 2px solid var(--solid); border-radius: 50%; }
  .brand-name { top: 132px; font-family: "Cinzel", serif; font-size: 26px; letter-spacing: 3px; color: var(--solid); }
  .brand-sub { top: 162px; font-family: "Cinzel", serif; font-size: 10.5px; letter-spacing: 3.6px; color: var(--solid); font-weight: 700; }
  .title-word { font-family: "Cinzel", serif; font-size: 66px; line-height: 1; }
  .title-top { top: 210px; }
  .title-bottom { top: 300px; }
  .title-mid { top: 279px; font-family: "Cormorant Garamond", serif; font-size: 17px; letter-spacing: 15px; padding-left: 15px; color: var(--solid); }
  .features { top: 396px; font-family: "Cormorant Garamond", serif; font-size: 15.5px; line-height: 18px; text-transform: uppercase; }
  .size { top: 512px; font-family: "Cormorant Garamond", serif; font-weight: 700; font-size: 23px; letter-spacing: 0.5px; }
</style>
</head>
<body>
<div class="sheet">
  <div class="proof-outline"></div>

  <section class="label gold pos-tl">
    <div class="backdrop paper" role="img" aria-label="Faint flowing wood-grain line pattern"></div>
    <span class="brand-mark"></span>
    <div class="line brand-name">Willow Drift</div>
    <div class="line brand-sub">HAUTE COLLECTION</div>
    <div class="line title-word title-top metal">MATTRESS</div>
    <div class="line title-mid">LUXURY QUILTED</div>
    <div class="line title-word title-bottom metal">PAD</div>
    <div class="line features metal">300 Thread Count<br>Stretch-to-Fit-Skirt<br>Allergy Deterrent<br>100% Cotton</div>
    <div class="line size metal">QUEEN</div>
  </section>

  <section class="label silver pos-tr">
    <div class="backdrop paper" role="img" aria-label="Faint flowing wood-grain line pattern"></div>
    <span class="brand-mark"></span>
    <div class="line brand-name">Willow Drift</div>
    <div class="line brand-sub">HAUTE COLLECTION</div>
    <div class="line title-word title-top metal">MATTRESS</div>
    <div class="line title-mid">LUXURY QUILTED</div>
    <div class="line title-word title-bottom metal">PAD</div>
    <div class="line features metal">300 Thread Count<br>Stretch-to-Fit-Skirt<br>Allergy Deterrent<br>100% Cotton</div>
    <div class="line size metal">QUEEN</div>
  </section>

  <section class="label gold pos-bl">
    <div class="backdrop satin" role="img" aria-label="Soft white satin fabric folds"></div>
    <span class="brand-mark"></span>
    <div class="line brand-name">Willow Drift</div>
    <div class="line brand-sub">HAUTE COLLECTION</div>
    <div class="line title-word title-top metal">MATTRESS</div>
    <div class="line title-mid">LUXURY QUILTED</div>
    <div class="line title-word title-bottom metal">PAD</div>
    <div class="line features metal">300 Thread Count<br>Stretch-to-Fit-Skirt<br>Allergy Deterrent<br>100% Cotton</div>
    <div class="line size metal">QUEEN</div>
  </section>

  <section class="label silver pos-br">
    <div class="backdrop satin" role="img" aria-label="Soft white satin fabric folds"></div>
    <span class="brand-mark"></span>
    <div class="line brand-name">Willow Drift</div>
    <div class="line brand-sub">HAUTE COLLECTION</div>
    <div class="line title-word title-top metal">MATTRESS</div>
    <div class="line title-mid">LUXURY QUILTED</div>
    <div class="line title-word title-bottom metal">PAD</div>
    <div class="line features metal">300 Thread Count<br>Stretch-to-Fit-Skirt<br>Allergy Deterrent<br>100% Cotton</div>
    <div class="line size metal">QUEEN</div>
  </section>
</div>
</body>
</html>
```